Car finance company business card

Create a nice business card for our car financing company , Visit our website www.birchlanefinance.com for the phone number and idea of the company look. Please do not be afraid to be creative. Name on card Is Marc-Antoine Beaulieu and phone number is on our website adress of business is
27816 Boulevard Saint-Orvel,
Mirabel, QC K4R 2T8

```html
<!DOCTYPE html>
<html lang="en">
<head>
<meta charset="utf-8">
<title>Birch Lane Finance – Business Card</title>
<link href="https://fonts.googleapis.com/css2?family=Rubik:wght@400;500;700&display=swap" rel="stylesheet">
<style>
  :root{
    --bg:#9a9a9a;
    --orange:#f07a30;
    --orange-deep:#dc4a3a;
    --accent:#f08a2e;
    --ink:#1c1c1c;
    --white:#ffffff;
    --mascot-fur:#ef7a2a;
    --mascot-suit:#4a55a8;
  }
  *{box-sizing:border-box;margin:0;padding:0}
  html,body{width:1200px;height:930px;overflow:hidden}
  body{background:var(--bg);font-family:"Rubik",sans-serif;position:relative}
  .card{position:absolute;width:560px;height:320px;border-radius:22px;box-shadow:0 10px 24px rgba(0,0,0,.25);overflow:hidden}
  .card--front{left:90px;top:90px;background:linear-gradient(90deg,var(--orange) 0%,#ea6a38 55%,var(--orange-deep) 100%)}
  .card--back{left:550px;top:520px;background:var(--white)}

  .brand{position:absolute;display:flex;align-items:center}
  .brand__mascot{border-radius:10px;background:linear-gradient(180deg,var(--mascot-fur) 0%,var(--mascot-fur) 55%,var(--mascot-suit) 100%);flex:none}
  .brand__name{font-weight:700;line-height:1.05;color:var(--ink);text-transform:uppercase;letter-spacing:.5px;white-space:nowrap}

  .card--front .brand{left:150px;top:70px;gap:14px}
  .card--front .brand__name{font-size:30px}
  .card--front .brand__mascot{width:86px;height:120px}

  .card--back .brand{left:28px;top:112px;gap:10px}
  .card--back .brand__name{font-size:22px}
  .card--back .brand__mascot{width:66px;height:96px}

  .front__web{position:absolute;left:0;right:0;bottom:34px;text-align:center;color:var(--white);font-size:14px;letter-spacing:.5px}

  .back__rule{position:absolute;left:280px;top:44px;width:2px;height:232px;background:linear-gradient(180deg,rgba(240,138,46,0),var(--accent) 30%,var(--accent) 70%,rgba(240,138,46,0))}
  .contact{position:absolute;left:298px;top:60px;right:14px;color:var(--ink);font-size:13px;line-height:1.45}
  .contact__name{color:var(--accent);font-size:17px;font-weight:500;text-transform:uppercase;letter-spacing:.2px;white-space:nowrap;margin-bottom:2px}
  .contact__title{margin-bottom:12px}
  .contact__addr{margin-bottom:10px}
  .contact__row{display:flex;align-items:center;gap:8px;white-space:nowrap}
  .contact__row svg{width:11px;height:11px;flex:none}
  .hl{color:var(--accent)}
</style>
</head>
<body>
  <section class="card card--front">
    <div class="brand">
      <span class="brand__name">Birch Lane<br>Finance</span>
      <div class="brand__mascot" role="img" aria-label="Cartoon fox mascot in blue overalls giving a thumbs up"></div>
    </div>
    <p class="front__web">www.birchlanefinance.com</p>
  </section>

  <section class="card card--back">
    <div class="brand">
      <span class="brand__name">Birch Lane<br>Finance</span>
      <div class="brand__mascot" role="img" aria-label="Cartoon fox mascot in blue overalls giving a thumbs up"></div>
    </div>
    <div class="back__rule"></div>
    <div class="contact">
      <p class="contact__name">Marc-Antoine Beaulieu</p>
      <p class="contact__title">Director</p>
      <p class="contact__addr">27816 Boulevard Saint-Orvel,<br>Mirabel, QC K4R 2T8</p>
      <p class="contact__row">
        <svg viewBox="0 0 12 12"><path d="M3 1l2 2.5-1.2 1.2a6 6 0 0 0 3.5 3.5L8.5 7 11 9l-1.5 2A9 9 0 0 1 1 2.5z" fill="var(--accent)"/></svg>
        (514) 555-0148
      </p>
      <p class="contact__row">
        <svg viewBox="0 0 12 12"><rect x="1" y="2.5" width="10" height="7" rx="1" fill="none" stroke="var(--accent)" stroke-width="1.2"/><path d="M1.5 3l4.5 3.5L10.5 3" fill="none" stroke="var(--accent)" stroke-width="1.2"/></svg>
        info@birchlanefinance.com
      </p>
      <p class="contact__row">
        <svg viewBox="0 0 12 12"><circle cx="6" cy="6" r="5" fill="none" stroke="var(--accent)" stroke-width="1.2"/><path d="M1 6h10M6 1c-2.5 3-2.5 7 0 10M6 1c2.5 3 2.5 7 0 10" fill="none" stroke="var(--accent)" stroke-width="1"/></svg>
        <span>www.<span class="hl">birchlanefinance</span>.com</span>
      </p>
    </div>
  </section>
</body>
</html>
```